Copper Heron Motor Services needs a logo design

I'm after a logo design for a new Female owned automotive repair workshop in the Queanbeyan/Canberra Australia Area.
We offer repairs on all passenger cars, 4wds and light trucks emphasising a strong honest work ethic and a genuine interest in the customer and their vehicles needs. With business details on the front of the card and what we offer on the back.
I would like a design with a phoenix in multiple colours maybe hovering over a flaming wheel or a car with wheels flaming with the phoenix hovering up out of the flames
Target Market(s)
All Vehicle users
Industry/Entity Type
Automotive
Contact Information for Business Card
On the front
Copper Heron Motor
Maree Tolland Owner/ Mechanic 0413527806
email maree@copperheronmotor.com.au
Website www.copperheronmotorworks.com.au
On the back
All Cars, 4WDs, Light trucks, makes and models
Log book servicing
General vehicle servicing
Major vehicle servicing
brake and clutch servicing and repairs
Suspension repairs
cooling systems
All major and minor mechanical repairs
minor electrical rewiring and repairs
Colors
Designer to choose colors to be used in the design.
Look and feel

```html
<!DOCTYPE html>
<html lang="en">
<head>
<meta charset="utf-8">
<title>Copper Heron Motor – Business Card</title>
<link href="https://fonts.googleapis.com/css2?family=Open+Sans:wght@600;700&family=Marcellus&family=Pinyon+Script&display=swap" rel="stylesheet">
<style>
  :root{
    --bg:#d9dadc;
    --card-dark:#050303;
    --card-warm:#2a0c08;
    --brand-orange:#f28a1e;
    --brand-red:#d8401c;
    --script-red:#e0542a;
    --cream:#f3e8cf;
    --soft-grey:#d8d2c8;
    --star:#f7efd9;
  }
  *{margin:0;padding:0;box-sizing:border-box}
  html,body{width:1200px;height:1200px;overflow:hidden;background:var(--bg)}
  .sheet{position:relative;width:1200px;height:1200px;display:flex;flex-direction:column;align-items:center;justify-content:center;gap:50px}
  .card{position:relative;width:960px;height:549px;overflow:hidden;
    background:radial-gradient(ellipse at 60% 55%,var(--card-warm) 0%,var(--card-dark) 70%);
    box-shadow:0 8px 24px rgba(0,0,0,.25)}

  /* front */
  .logo{position:absolute;left:150px;top:120px;display:flex;align-items:center;gap:18px}
  .logo-dot{width:46px;height:46px;border-radius:50%;background:var(--brand-orange)}
  .logo-name{font-family:"Open Sans",sans-serif;font-weight:700;font-size:34px;color:var(--brand-orange);letter-spacing:.5px;text-transform:uppercase}
  .person{position:absolute;right:70px;top:200px;text-align:right}
  .person-name{font-family:"Pinyon Script",cursive;font-size:56px;color:var(--script-red);line-height:1}
  .person-role{font-family:"Marcellus",serif;font-size:24px;color:var(--soft-grey);margin-top:8px}
  .contact{position:absolute;right:70px;bottom:70px;list-style:none;text-align:right;font-family:"Marcellus",serif;font-size:24px;color:var(--soft-grey)}
  .contact li{display:flex;align-items:center;justify-content:flex-end;gap:14px;margin-top:12px}
  .contact svg{width:24px;height:24px;fill:var(--brand-red)}

  /* back */
  .services{position:absolute;left:70px;top:50px;list-style:none;font-family:"Marcellus",serif;font-size:25px;color:var(--cream);line-height:1.55}
  .services li{display:flex;align-items:center;gap:16px}
  .services svg{width:18px;height:18px;fill:var(--star);flex:none}
  .phoenix-art{position:absolute;right:40px;bottom:20px;width:440px;height:360px;border-radius:50%;
    background:radial-gradient(ellipse at 55% 50%,rgba(242,120,40,.75) 0%,rgba(230,70,40,.45) 35%,rgba(60,140,170,.25) 60%,rgba(0,0,0,0) 75%)}
</style>
</head>
<body>
<main class="sheet">

  <section class="card card-front" aria-label="Card front">
    <div class="logo">
      <span class="logo-dot"></span>
      <span class="logo-name">Copper Heron Motor</span>
    </div>
    <div class="person">
      <p class="person-name">Maree Tolland</p>
      <p class="person-role">Owner/ Mechanic</p>
    </div>
    <ul class="contact">
      <li>0413527806
        <svg viewBox="0 0 24 24"><path d="M6.6 10.8a15.1 15.1 0 0 0 6.6 6.6l2.2-2.2a1 1 0 0 1 1-.25 11.4 11.4 0 0 0 3.6.57 1 1 0 0 1 1 1V20a1 1 0 0 1-1 1A17 17 0 0 1 3 4a1 1 0 0 1 1-1h3.5a1 1 0 0 1 1 1c0 1.25.2 2.45.57 3.57a1 1 0 0 1-.25 1z"/></svg>
      </li>
      <li>maree@copperheronmotor.com.au
        <svg viewBox="0 0 24 24"><path d="M2 5h20v14H2z" opacity=".95"/><path d="M2 5l10 8 10-8" fill="none" stroke="#2a0c08" stroke-width="1.6"/></svg>
      </li>
    </ul>
  </section>

  <section class="card card-back" aria-label="Card back">
    <ul class="services">
      <li><svg viewBox="0 0 24 24"><path d="M12 2l3 7h7l-5.5 4.5 2 7.5L12 16.5 5.5 21l2-7.5L2 9h7z"/></svg>All Cars, 4wds, Light Trucks, Makes And Models</li>
      <li><svg viewBox="0 0 24 24"><path d="M12 2l3 7h7l-5.5 4.5 2 7.5L12 16.5 5.5 21l2-7.5L2 9h7z"/></svg>Log Book Servicing</li>
      <li><svg viewBox="0 0 24 24"><path d="M12 2l3 7h7l-5.5 4.5 2 7.5L12 16.5 5.5 21l2-7.5L2 9h7z"/></svg>General Vehicle Servicing</li>
      <li><svg viewBox="0 0 24 24"><path d="M12 2l3 7h7l-5.5 4.5 2 7.5L12 16.5 5.5 21l2-7.5L2 9h7z"/></svg>Major Vehicle Servicing</li>
      <li><svg viewBox="0 0 24 24"><path d="M12 2l3 7h7l-5.5 4.5 2 7.5L12 16.5 5.5 21l2-7.5L2 9h7z"/></svg>Brake And Clutch Servicing And Repairs</li>
      <li><svg viewBox="0 0 24 24"><path d="M12 2l3 7h7l-5.5 4.5 2 7.5L12 16.5 5.5 21l2-7.5L2 9h7z"/></svg>Suspension Repairs</li>
      <li><svg viewBox="0 0 24 24"><path d="M12 2l3 7h7l-5.5 4.5 2 7.5L12 16.5 5.5 21l2-7.5L2 9h7z"/></svg>Cooling Systems</li>
      <li><svg viewBox="0 0 24 24"><path d="M12 2l3 7h7l-5.5 4.5 2 7.5L12 16.5 5.5 21l2-7.5L2 9h7z"/></svg>All Major And Minor Mechanical Repairs</li>
      <li><svg viewBox="0 0 24 24"><path d="M12 2l3 7h7l-5.5 4.5 2 7.5L12 16.5 5.5 21l2-7.5L2 9h7z"/></svg>Minor Electrical Rewiring And Repairs</li>
    </ul>
    <div class="phoenix-art" role="img" aria-label="Colourful painted bird rising in orange, red, blue and green flames"></div>
  </section>

</main>
</body>
</html>
```